Brochure for Home Improvement Startup

We need an eye-catching, informative, and easy to read brochure design to help explain our services to our target audience which include baby boomers and seniors.

Baby

```html
<!DOCTYPE html>
<html lang="en">
<head>
<meta charset="utf-8">
<title>NestWell Trifold Brochure</title>
<link rel="stylesheet" href="https://fonts.googleapis.com/css2?family=Montserrat+Alternates:wght@500;600;700&family=Lato:ital,wght@0,400;0,700;1,400&display=swap">
<style>
  :root{
    --magenta:#c2186f;
    --ink:#2b2b2e;
    --slate:#59595d;
    --band:#6a6a6e;
    --paper:#ffffff;
    --bg:#e9e9ea;
    --muted:#9a9a9e;
    --lawn:#7fbf2f;
  }
  *{box-sizing:border-box;margin:0;padding:0}
  html,body{width:1200px;height:1200px;overflow:hidden;background:var(--bg)}
  body{font-family:'Lato',sans-serif;color:var(--ink)}
  .brochure{position:absolute;left:30px;top:160px;width:1140px;height:880px;display:flex;box-shadow:0 10px 30px rgba(0,0,0,.15)}
  .panel{position:relative;width:380px;height:880px;background:var(--paper);overflow:hidden}
  .panel + .panel{border-left:1px solid #e2e2e4}
  .shapes{position:absolute;inset:0;width:100%;height:100%}

  /* left panel */
  .info{position:absolute;left:34px;top:34px;right:30px;font-size:11.5px;line-height:1.45;font-style:italic}
  .info h3{font-family:'Montserrat Alternates',sans-serif;font-style:normal;font-weight:600;color:var(--magenta);font-size:13px;margin:16px 0 6px}
  .info h3:first-child{margin-top:0}
  .info ul{list-style:none}
  .info li{position:relative;padding-left:18px;margin-bottom:6px}
  .info li svg{position:absolute;left:0;top:3px;width:10px;height:10px}

  /* middle panel */
  .brand{font-family:'Montserrat Alternates',sans-serif;font-weight:600;color:var(--slate);display:flex;align-items:center;gap:8px}
  .brand .mark{width:12px;height:12px;background:var(--magenta)}
  .back-brand{position:absolute;left:0;right:0;top:485px;justify-content:center;font-size:32px}
  .contact{position:absolute;left:0;right:0;top:560px;text-align:center;font-family:'Montserrat Alternates',sans-serif;font-weight:500;font-size:14px;color:var(--ink)}
  .contact .item{display:flex;flex-direction:column;align-items:center;margin-bottom:14px}
  .contact .icon{width:30px;height:30px;border-radius:50%;background:var(--slate);display:flex;align-items:center;justify-content:center;margin-bottom:6px}

  /* right panel */
  .front-brand{position:absolute;right:34px;top:26px;font-size:34px}
  .headline{position:absolute;left:30px;top:478px;font-family:'Montserrat Alternates',sans-serif}
  .headline .lead{color:var(--magenta);font-weight:700;font-size:30px;display:block}
  .headline .main{color:var(--ink);font-weight:600;font-size:30px;letter-spacing:1px;display:block;margin-top:-4px}
  .about{position:absolute;left:30px;right:30px;top:568px;font-size:12.5px;line-height:1.4}
  .about h4{font-family:'Montserrat Alternates',sans-serif;font-weight:600;color:var(--magenta);font-size:14px;margin:8px 0 3px}
  .about p{text-align:justify}
</style>
</head>
<body>
<main class="brochure">

  <!-- Inside flap -->
  <section class="panel panel-info">
    <div class="info">
      <h3>Other information</h3>
      <ul>
        <li><svg viewBox="0 0 10 10"><rect width="4" height="4" fill="#c2186f"/><rect x="6" width="4" height="4" fill="#59595d"/><rect y="6" width="4" height="4" fill="#59595d"/><rect x="6" y="6" width="4" height="4" fill="#c2186f"/></svg>Treating fall injuries is very costly. In 2015, direct medical costs for falls—what patients and insurance companies pay—totaled $34 billion... and it may reach $67.7 billion by 2020.</li>
        <li><svg viewBox="0 0 10 10"><rect width="4" height="4" fill="#c2186f"/><rect x="6" width="4" height="4" fill="#59595d"/><rect y="6" width="4" height="4" fill="#59595d"/><rect x="6" y="6" width="4" height="4" fill="#c2186f"/></svg>Each year, 2.8 million people 65 and older are treated in emergency departments because of falls.</li>
        <li><svg viewBox="0 0 10 10"><rect width="4" height="4" fill="#c2186f"/><rect x="6" width="4" height="4" fill="#59595d"/><rect y="6" width="4" height="4" fill="#59595d"/><rect x="6" y="6" width="4" height="4" fill="#c2186f"/></svg>Over 800,000 patients a year are hospitalized because of a fall injury, most often because of a broken hip or head injury.</li>
        <li><svg viewBox="0 0 10 10"><rect width="4" height="4" fill="#c2186f"/><rect x="6" width="4" height="4" fill="#59595d"/><rect y="6" width="4" height="4" fill="#59595d"/><rect x="6" y="6" width="4" height="4" fill="#c2186f"/></svg>Each year at least 250,000 older people are hospitalized for hip fractures. More than 95% of hip fractures are caused by falling, usually by falling sideways.</li>
        <li><svg viewBox="0 0 10 10"><rect width="4" height="4" fill="#c2186f"/><rect x="6" width="4" height="4" fill="#59595d"/><rect y="6" width="4" height="4" fill="#59595d"/><rect x="6" y="6" width="4" height="4" fill="#c2186f"/></svg>The average hospital cost for a fall injury is $35,000.</li>
        <li><svg viewBox="0 0 10 10"><rect width="4" height="4" fill="#c2186f"/><rect x="6" width="4" height="4" fill="#59595d"/><rect y="6" width="4" height="4" fill="#59595d"/><rect x="6" y="6" width="4" height="4" fill="#c2186f"/></svg>The costs of treating fall injuries goes up with age.</li>
      </ul>
      <h3>Health agencies state four things you can do to prevent falls:</h3>
      <ul>
        <li><svg viewBox="0 0 10 10"><rect width="4" height="4" fill="#c2186f"/><rect x="6" width="4" height="4" fill="#59595d"/><rect y="6" width="4" height="4" fill="#59595d"/><rect x="6" y="6" width="4" height="4" fill="#c2186f"/></svg>Begin an exercise program to improve your leg strength &amp; balance</li>
        <li><svg viewBox="0 0 10 10"><rect width="4" height="4" fill="#c2186f"/><rect x="6" width="4" height="4" fill="#59595d"/><rect y="6" width="4" height="4" fill="#59595d"/><rect x="6" y="6" width="4" height="4" fill="#c2186f"/></svg>Ask your doctor or pharmacist to review your medicines</li>
        <li><svg viewBox="0 0 10 10"><rect width="4" height="4" fill="#c2186f"/><rect x="6" width="4" height="4" fill="#59595d"/><rect y="6" width="4" height="4" fill="#59595d"/><rect x="6" y="6" width="4" height="4" fill="#c2186f"/></svg>Get annual eye check-ups &amp; update your eyeglasses</li>
      </ul>
      <h3>Make your home safer by:</h3>
      <ul>
        <li><svg viewBox="0 0 10 10"><circle cx="5" cy="5" r="4.2" fill="none" stroke="#c2186f" stroke-width="1.2"/><path d="M3 5.2l1.5 1.5L7.2 3.8" fill="none" stroke="#c2186f" stroke-width="1.2"/></svg>Removing clutter &amp; tripping hazards</li>
        <li><svg viewBox="0 0 10 10"><circle cx="5" cy="5" r="4.2" fill="none" stroke="#c2186f" stroke-width="1.2"/><path d="M3 5.2l1.5 1.5L7.2 3.8" fill="none" stroke="#c2186f" stroke-width="1.2"/></svg>Putting railings on all stairs &amp; adding grab bars in the bathroom</li>
        <li><svg viewBox="0 0 10 10"><circle cx="5" cy="5" r="4.2" fill="none" stroke="#c2186f" stroke-width="1.2"/><path d="M3 5.2l1.5 1.5L7.2 3.8" fill="none" stroke="#c2186f" stroke-width="1.2"/></svg>Having good lighting, especially on stairs</li>
      </ul>
    </div>
    <svg class="shapes" viewBox="0 0 380 880" aria-hidden="true">
      <defs>
        <linearGradient id="houseTone" x1="0" y1="0" x2="0" y2="1">
          <stop offset="0" stop-color="#b8d3e6"/>
          <stop offset="0.35" stop-color="#c8b497"/>
          <stop offset="0.75" stop-color="#9a8067"/>
          <stop offset="1" stop-color="#79b23a"/>
        </linearGradient>
      </defs>
      <polygon points="0,640 380,720 380,880 0,880" fill="url(#houseTone)" role="img" aria-label="Photo of a large stone family house with garages and a green lawn"/>
      <polygon points="0,612 110,635 0,650" fill="var(--magenta)"/>
      <polygon points="250,880 380,815 380,835 290,880" fill="var(--magenta)"/>
      <polygon points="290,880 380,835 380,880" fill="var(--lawn)"/>
    </svg>
  </section>

  <!-- Back panel -->
  <section class="panel panel-back">
    <svg class="shapes" viewBox="0 0 380 880" aria-hidden="true">
      <defs>
        <linearGradient id="brickTone" x1="0" y1="0" x2="0" y2="1">
          <stop offset="0" stop-color="#ffffff"/>
          <stop offset="0.3" stop-color="#c9a79a"/>
          <stop offset="1" stop-color="#8c4a3a"/>
        </linearGradient>
        <linearGradient id="fadeHouse" x1="0" y1="0" x2="0" y2="1">
          <stop offset="0" stop-color="#eeeeef"/>
          <stop offset="1" stop-color="#ffffff"/>
        </linearGradient>
      </defs>
      <polygon points="0,0 380,0 380,420 0,330" fill="url(#brickTone)" role="img" aria-label="Photo of a brick house entrance with a dark front door under a small porch roof"/>
      <polygon points="0,346 380,436 380,880 0,880" fill="url(#fadeHouse)" role="img" aria-label="Faint background photo of a house"/>
      <polygon points="0,330 380,420 380,436 0,346" fill="var(--band)"/>
      <polygon points="0,780 130,880 100,880 0,805" fill="var(--magenta)"/>
    </svg>
    <div class="brand back-brand"><span>NestWell</span><span class="mark"></span></div>
    <div class="contact">
      <div class="item">
        <span class="icon"><svg width="14" height="16" viewBox="0 0 14 16"><path d="M7 1a5 5 0 0 0-5 5c0 4 5 9 5 9s5-5 5-9a5 5 0 0 0-5-5z" fill="#c2186f"/><circle cx="7" cy="6" r="1.8" fill="#fff"/></svg></span>
        <span>1480 harbor view rd,<br>lakeside, wa 98000, usa</span>
      </div>
      <div class="item">
        <span class="icon"><svg width="14" height="14" viewBox="0 0 14 14"><path d="M3 1l2 3-1.3 1.3a8 8 0 0 0 5 5L10 9l3 2-1 2.5C6 13 1 8 .5 2z" fill="#c2186f"/></svg></span>
        <span>555.014.2290</span>
      </div>
      <div class="item">
        <span class="icon"><svg width="16" height="12" viewBox="0 0 16 12"><rect x="1" y="1" width="14" height="10" fill="none" stroke="#c2186f" stroke-width="1.5"/><path d="M1 1l7 5 7-5" fill="none" stroke="#c2186f" stroke-width="1.5"/></svg></span>
        <span>hello@nestwellliving.com</span>
      </div>
    </div>
  </section>

  <!-- Front cover -->
  <section class="panel panel-cover">
    <svg class="shapes" viewBox="0 0 380 880" aria-hidden="true">
      <defs>
        <linearGradient id="coupleTone" x1="0" y1="0" x2="1" y2="1">
          <stop offset="0" stop-color="#e6ddd6"/>
          <stop offset="0.45" stop-color="#a8654e"/>
          <stop offset="1" stop-color="#7aa7d8"/>
        </linearGradient>
      </defs>
      <polygon points="0,90 380,90 380,462 0,400" fill="url(#coupleTone)" role="img" aria-label="Photo of a smiling senior couple standing in front of their brick home"/>
      <polygon points="0,400 380,462 380,482 0,414" fill="var(--band)"/>
      <polygon points="262,880 380,838 380,850 292,880" fill="var(--magenta)"/>
      <polygon points="292,880 380,850 380,880" fill="var(--band)"/>
    </svg>
    <div class="brand front-brand"><span>NestWell</span><span class="mark"></span></div>
    <h1 class="headline"><span class="lead">We Create</span><span class="main">BETTER HOMES</span></h1>
    <div class="about">
      <h4>Mission</h4>
      <p>To Improve the technology, ergonomics, safety, and maintenance of our client's homes to enhance their overall quality of life.</p>
      <h4>Focus</h4>
      <p>We deliver light home modification service to seniors and boomers so their homes continue to meet their changing needs. Specifically, we provide consultation and aging in place assessments to homeowners, sales, and installation of high quality grab bars, threshold ramps, lighting, and smart home technology as well ongoing home maintenance through a home "Fitness Plan".</p>
    </div>
  </section>

</main>
</body>
</html>
```